Mergers and Acquisitions Business Seeks Fresh Website Design

IMPORTANT: Please only design the Homepage, for the contest. If you win the contest, you will design the inner pages, as see in the attached document 'Travik 2025 website wireframes."
Design a new website for Travik at travik.global. Maintaining current Impact and Open Sans fonts, or using open-source alternatives from Google Fonts.
Enhance the design with a premium feel, impactful visuals, and dynamic content. We want the new design to focus on generating high-quality inquiries, strong calls to action, and consistent branding.
Industry/Entity Type
Mergers and Acquisitions
Number of Pages Required
5+ page
Font styles to use
Other font styles liked:
- See Website Brief file
Requirements
Must have
- Consistency in layout, colours, fonts and overall design
Should not have
- Very bright colours, hard to read fonts, unlicensed images and fonts

```html
<!DOCTYPE html>
<html lang="en">
<head>
<meta charset="utf-8">
<title>Travik – Deal Origination</title>
<link href="https://fonts.googleapis.com/css2?family=Anton&family=Open+Sans:wght@400;600;700&display=swap" rel="stylesheet">
<style>
:root{
  --purple:#5e2374;
  --purple-mid:#6d2f87;
  --purple-light:#8a4ba3;
  --accent:#f6c21c;
  --ink:#3b3b3b;
  --grey-bg:#f1f1f1;
  --map:#cfd6da;
  --white:#ffffff;
}
*{box-sizing:border-box;margin:0;padding:0}
html,body{width:1200px;height:4651px;overflow:hidden;background:var(--white)}
body{position:relative;font-family:"Open Sans",Arial,sans-serif;color:var(--ink)}
.abs{position:absolute}
.display{font-family:"Anton",Impact,sans-serif;font-weight:400}
.section-title{position:absolute;left:0;width:1200px;text-align:center;font-family:"Anton",Impact,sans-serif;color:var(--purple);font-size:36px;line-height:1}

/* header */
.site-header{top:0;left:0;width:1200px;height:72px;background:var(--purple)}
.brand{left:182px;top:4px;font-family:"Anton",Impact,sans-serif;color:var(--white);font-size:48px;line-height:60px}
.main-nav{left:374px;top:0;height:72px;display:flex;align-items:center;gap:32px;font-family:"Anton",Impact,sans-serif;font-size:13px;letter-spacing:.3px;color:var(--white)}
.main-nav .active{color:var(--accent)}
.phone-pill{left:884px;top:22px;width:142px;height:28px;border-radius:14px;background:var(--white);display:flex;align-items:center;gap:6px;padding-left:10px;font-family:"Anton",Impact,sans-serif;font-size:12px;color:#111}
.phone-pill .flag{width:22px;height:14px;background:#2a4d9b;border-radius:2px}

/* hero */
.hero{top:72px;left:0;width:1200px;height:440px;background:linear-gradient(90deg,#f4f4f4 0%,#eceaea 30%,#cfc6c2 60%,#8a7a72 100%)}
.hero-title{left:78px;top:180px;font-family:"Anton",Impact,sans-serif;color:var(--purple);font-size:52px;line-height:54px}
.hero-title .bar{display:inline-block;width:10px;height:42px;background:var(--accent);vertical-align:-2px;margin-right:4px}
.hero-select{display:inline-flex;justify-content:space-between;align-items:center;width:190px;height:42px;border:3px solid var(--purple);border-radius:10px;padding:0 14px;font-size:26px;vertical-align:6px;margin-left:8px}

/* intro */
.intro{left:180px;top:630px;width:840px;text-align:center;font-size:13px;line-height:17px;color:#555}
.intro p{margin-bottom:14px}
.panel{border-radius:26px;background:linear-gradient(135deg,var(--purple) 0%,var(--purple-light) 100%);color:var(--white)}
.pitch{left:175px;top:809px;width:385px;height:269px;text-align:center;padding:60px 28px 0}
.pitch strong{display:block;font-size:20px;line-height:27px;font-family:"Open Sans",sans-serif;font-weight:700;margin-bottom:30px}
.pitch span{font-size:19px;line-height:26px;font-family:"Open Sans",sans-serif;font-stretch:condensed}
.benefits{left:637px;top:809px;width:386px;height:269px;padding:14px 22px 0 30px;list-style:none;font-size:12.5px;line-height:15px}
.benefits li{position:relative;margin-bottom:17px}
.benefits li::before{content:"";position:absolute;left:-12px;top:6px;width:5px;height:5px;border-radius:50%;background:var(--white)}

/* video */
.video{top:1128px;left:0;width:1200px;height:678px;background:var(--grey-bg)}
.video-title{left:0;top:62px;width:1200px;text-align:center;font-family:"Anton",Impact,sans-serif;font-size:46px;line-height:58px;color:#444}
.video-title em{font-style:normal;color:var(--purple)}
.play{left:486px;top:277px}
.captions{left:918px;top:568px;font-family:"Anton",Impact,sans-serif;font-size:24px;color:var(--purple)}
.captions em{font-style:normal;color:#444}
.controls{left:11px;top:632px;width:1178px;height:29px}
.controls .btn{position:absolute;left:0;top:0;width:50px;height:29px;background:#111}
.controls .track{position:absolute;left:55px;top:0;right:0;height:29px;background:#111}
.side-tools{left:1171px;top:1134px}
.side-tools span{display:block;width:22px;height:22px;background:#111;border-radius:3px;margin-bottom:6px}

/* work for */
.workfor{left:175px;top:1913px;width:848px;height:307px;border-radius:26px;overflow:hidden;background:var(--purple)}
.workfor .media{position:absolute;left:0;top:0;width:466px;height:307px;background:linear-gradient(135deg,#0b1e33 0%,#1f4d74 55%,#6a7f8e 100%)}
.workfor .copy{position:absolute;left:466px;top:0;width:382px;height:307px;text-align:center;color:var(--white);padding-top:22px;background:linear-gradient(135deg,var(--purple),var(--purple-light))}
.workfor h3{font-family:"Anton",Impact,sans-serif;font-weight:400;font-size:36px;line-height:44px}
.workfor p{font-size:13px;line-height:17px;margin-top:12px}
.workfor h4{font-family:"Anton",Impact,sans-serif;font-weight:400;font-size:22px;margin-top:14px}
.workfor .ctas{display:flex;justify-content:center;gap:26px;margin-top:22px}
.pill{display:inline-block;background:var(--white);color:var(--purple);border-radius:8px;font-family:"Anton",Impact,sans-serif;font-size:12px;line-height:25px;padding:0 16px;letter-spacing:.3px}

/* numbers */
.numbers{left:292px;top:2341px;width:614px;height:190px;border:3px solid var(--purple);border-radius:24px}
.numbers .ratio{position:absolute;left:126px;top:12px;font-family:"Anton",Impact,sans-serif;color:var(--purple);font-size:136px;line-height:160px}
.numbers .note{position:absolute;left:320px;top:62px;font-size:20px;line-height:30px;color:#444;font-stretch:condensed}

/* case studies */
.case{width:388px;height:307px;border-radius:26px;overflow:hidden;background:var(--purple)}
.case .media{height:240px;background:linear-gradient(160deg,#8fb8dc 0%,#c9b9a5 55%,#8d7a66 100%)}
.case.site .media{background:linear-gradient(160deg,#7f858a 0%,#b4b8ba 50%,#c76a3a 100%)}
.case .caption{height:67px;color:var(--white);text-align:center;font-size:11.5px;line-height:15px;padding-top:11px;font-stretch:condensed;background:linear-gradient(90deg,var(--purple),var(--purple-light))}
.more{left:531px;top:3319px;width:139px;height:26px;border-radius:8px;background:var(--purple);color:var(--white);text-align:center;font-family:"Anton",Impact,sans-serif;font-size:12px;line-height:26px}

/* insights */
.insight{top:3444px;width:168px;height:226px;border-radius:24px;padding:14px 14px 0;text-align:center;font-size:11px;line-height:14px}
.insight .thumb{height:162px;border-radius:18px;background:rgba(255,255,255,.22);margin-bottom:10px}
.dot{top:3692px;width:34px;height:34px;border-radius:50%;border:3px solid var(--purple)}
.dot.on{background:var(--purple)}

/* map & offices */
.map{left:175px;top:3854px;width:848px;height:442px;background:linear-gradient(180deg,#e3e8eb 0%,var(--map) 100%);border-radius:8px}
.office{font-size:12.5px;line-height:15px;color:#555}
.office h5{font-family:"Open Sans",sans-serif;font-weight:700;font-size:17px;color:var(--purple);line-height:20px}
.office-uk{left:300px;top:4328px;width:263px;text-align:right}
.office-apac{left:635px;top:4328px;width:260px}

/* footer */
.footer-rule{left:175px;top:4458px;width:848px;height:1px;background:#bbb}
.fcol{top:4480px;font-size:12.5px;line-height:19px;color:#555}
.fcol h6{font-family:"Open Sans",sans-serif;font-weight:700;font-size:16px;color:var(--purple);line-height:22px;letter-spacing:.5px}
.fbtn{display:block;width:139px;height:26px;border-radius:7px;background:var(--purple);color:var(--white);text-align:center;font-family:"Anton",Impact,sans-serif;font-size:12px;line-height:26px;margin-top:9px}
.social{display:inline-block;width:26px;height:26px;border-radius:50%;background:var(--purple);vertical-align:middle;margin-left:8px}
.legal{left:0;top:4614px;width:1200px;height:37px;background:var(--purple);color:var(--white);font-size:12.5px;line-height:37px;text-align:center;word-spacing:1px}
.legal span{margin:0 10px}
</style>
</head>
<body>

<header class="abs site-header">
  <div class="abs brand">travik</div>
  <nav class="abs main-nav">
    <span class="active">CLIENTS</span><span>SERVICES</span><span>CASE STUDIES</span><span>BLOG</span><span>ABOUT US</span><span>CONTACT US</span>
  </nav>
  <div class="abs phone-pill"><span class="flag"></span>+44 1632 960 000</div>
</header>

<section class="abs hero" role="img" aria-label="Photo of smiling business people shaking hands and applauding a completed deal">
</section>
<h1 class="abs hero-title"><span class="bar"></span>DEAL<br>ORIGINATION<br>FOR<span class="hero-select"><span>YOU?</span><span style="font-size:20px">v</span></span></h1>

<h2 class="section-title" style="top:565px">Exclusive Deals, Reduced Risk, Stronger Leverage</h2>
<div class="abs intro">
  <p>We consistently deliver high-quality deals, bypassing the crowded open market. Imagine a pipeline filled with precise targets, aligned with your acquisition goals.</p>
  <p>Our approach minimises execution risk. We bring forward only well-matched prospects backed by transparent tracking and guidance. By specialising in off-market exclusivity, we enhance your negotiation leverage, reducing competition and securing favourable terms for both parties.</p>
  <p>We focus on quality over quantity, building high-trust seller relationships. Gain a competitive edge with our deep market knowledge and highly targeted outreach, expanding your market share. Travik enables you to acquire smarter, faster, and more effectively.</p>
</div>

<div class="abs panel pitch">
  <strong>Travik empowers acquirers to outpace competitors by consistently delivering</strong>
  <span>high-response, off-market deal flow, without adding headcount or overhead.</span>
</div>
<ul class="abs panel benefits">
  <li><b>Find the ideal fit</b> - Target businesses that match your exact criteria</li>
  <li><b>More options</b> - Access businesses that aren't public listed</li>
  <li><b>No noise</b> - Avoid disruption from ad visors and brokers</li>
  <li><b>Higher-quality deals</b> - Engage with owners who prefer a discreet sale</li>
  <li><b>More control</b> - Move at your own pace, without broker pressure</li>
  <li><b>Stronger relationships</b> - Direct contact with business owners</li>
</ul>

<section class="abs video">
  <h2 class="abs video-title">DISCOVER HOW TO <em>INCREASE</em><br>YOUR <em>DEAL FLOW</em> TODAY</h2>
  <svg class="abs play" width="230" height="230" viewBox="0 0 230 230" aria-label="Play video"><circle cx="115" cy="115" r="115" fill="#5e2374"/><path d="M86 66 L86 164 L166 115 Z" fill="#fff" stroke="#fff" stroke-width="10" stroke-linejoin="round"/></svg>
  <div class="abs captions"><em>CAPTIONS</em> IF NEEDED</div>
  <svg class="abs" style="left:1040px;top:528px" width="150" height="100" viewBox="0 0 150 100"><path d="M10 30 C50 -5 110 0 132 60" fill="none" stroke="#5e2374" stroke-width="7"/><path d="M112 52 L134 90 L148 48" fill="none" stroke="#5e2374" stroke-width="7" stroke-linejoin="round"/></svg>
  <div class="abs controls"><span class="btn"></span><span class="track"></span>
    <svg class="abs" style="left:18px;top:8px" width="14" height="14"><path d="M1 1 L13 7 L1 13Z" fill="#fff"/></svg></div>
</section>
<div class="abs side-tools"><span></span><span></span><span></span></div>

<h2 class="section-title" style="top:1852px">We Work For</h2>
<div class="abs workfor">
  <div class="media" role="img" aria-label="Photo of a hand touching a digital private equity interface"></div>
  <div class="copy">
    <h3>Private Equity</h3>
    <p>Expand your pipeline beyond<br>traditional brokers and geographic boundaries.</p>
    <h4>If You Want Ideal Flow, Let's Talk</h4>
    <p>There is only so much you can tell from reviewing<br>our website, the best way to explore is to have<br>a short meeting with one of our team.</p>
    <div class="ctas"><span class="pill">CALL 01632 960 000</span><span class="pill">CONTACT TRAVIK</span></div>
  </div>
</div>

<h2 class="section-title" style="top:2282px">Travik the Numbers</h2>
<div class="abs numbers">
  <svg class="abs" style="left:38px;top:52px" width="86" height="86" viewBox="0 0 86 86"><circle cx="43" cy="43" r="37" fill="none" stroke="#5e2374" stroke-width="6"/><path d="M26 44 L40 56 L56 28" fill="none" stroke="#5e2374" stroke-width="6" stroke-linecap="round" stroke-linejoin="round"/><path d="M30 4 L56 4" stroke="#5e2374" stroke-width="6" stroke-linecap="round"/></svg>
  <div class="ratio">1:5</div>
  <div class="note">For every 1 target approached,<br>we analyse at least 5 companies</div>
</div>

<h2 class="section-title" style="top:2576px">Recent Case Studies</h2>
<div class="abs case" style="left:175px;top:2639px"><div class="media" role="img" aria-label="Photo of engineers in hard hats reviewing a construction site"></div><div class="caption">Fire Safety Focussed Investment Group<br><b>Acquired</b><br>A bespoke Fire and Security Solutions Business</div></div>
<div class="abs case site" style="left:637px;top:2639px"><div class="media" role="img" aria-label="Aerial photo of workers fixing rebar on a building site"></div><div class="caption">Leading Labour Recruitment Company<br><b>Acquired</b><br>An Established Constrution &amp; Recruitment Firm</div></div>
<div class="abs case" style="left:175px;top:2989px"><div class="media" role="img" aria-label="Photo of engineers in hard hats reviewing a construction site"></div><div class="caption">Fire Safety Focussed Investment Group<br><b>Acquired</b><br>A bespoke Fire and Security Solutions Business</div></div>
<div class="abs case site" style="left:637px;top:2989px"><div class="media" role="img" aria-label="Aerial photo of workers fixing rebar on a building site"></div><div class="caption">Leading Labour Recruitment Company<br><b>Acquired</b><br>An Established Constrution &amp; Recruitment Firm</div></div>
<div class="abs more">MORE CASE STUDIES</div>

<h2 class="section-title" style="top:3383px">M&amp;A Insights &amp; Latest Trends</h2>
<article class="abs panel insight" style="left:175px"><div class="thumb" role="img" aria-label="Article thumbnail"></div>Why Off Market is Key for the Motivated Buyer</article>
<article class="abs panel insight" style="left:393px"><div class="thumb" role="img" aria-label="Article thumbnail"></div>Is There a Suitable Business for Sale Near ME?</article>
<article class="abs panel insight" style="left:637px"><div class="thumb" role="img" aria-label="Article thumbnail"></div>5 Ways to Increase Your Chances of Selling Your Business</article>
<article class="abs panel insight" style="left:854px"><div class="thumb" role="img" aria-label="Article thumbnail"></div>How to Finance Your Next Business Acquisition</article>
<span class="abs dot on" style="left:463px"></span><span class="abs dot" style="left:523px"></span><span class="abs dot" style="left:582px"></span><span class="abs dot" style="left:642px"></span><span class="abs dot" style="left:701px"></span>

<h2 class="section-title" style="top:3778px">Regional and Cross-Border Deal Makers</h2>
<div class="abs map" role="img" aria-label="World map with the UK and Europe highlighted in purple"></div>

<div class="abs office office-uk"><h5>UK &amp; EuropeOffice</h5>Fourth Floor<br>Kestrel Court House Reading<br>RG1 9ZX<br>Contact: +44 (0) 1632 960 000</div>
<div class="abs office office-apac"><h5>APAC Office</h5>12 Quayline Street<br>Marrow Point<br>NSW 2000<br>Australia<br>Contact: +61 (0) 491 570 110</div>

<div class="abs footer-rule"></div>
<div class="abs fcol" style="left:175px"><h6>CLIENTS</h6>Private Equity<br>Trade Buyers<br>Management Buy In<br>Search Funds<br>Corporate Finance</div>
<div class="abs fcol" style="left:386px"><h6>SERVICES</h6>DealOrigination<br>Single Acquisitions<br>Buy and Build<br>Bolt-OnAcquisitions<br>Cross Border/ International</div>
<div class="abs fcol" style="left:635px;top:4502px">Acquisition Finance<br>Negotiation Support<br>Due Diligence</div>
<div class="abs fcol" style="left:884px;width:139px;text-align:right"><h6>CONTACT<span class="social"></span></h6>+44 (0) 1632 960 000<span class="fbtn">CONTACT TRAVIK</span><span class="fbtn">BOOK APPOINTMENT</span></div>

<footer class="abs legal"><span>© Travik limited. All rights reserved</span><span>Policies Terms of Use</span>Privacy Policy<span>Contact Us</span></footer>

</body>
</html>
```